Engineering Consultants Brochure Design

We need a brochure design for our company Kestrel Ridge Systems. We are engineering consultants, who get involved in site survey all the way through to manufacture. Our main clients are from the oil and gas industry and we are best known for our computational analysis - we are leaders in the field.

We have a concept design which has all the components we are happy with, but as Engineers our artistic skills are not up to much. We would like designers to take our mock up and add more artistic flair. We are looking for a 3 page fold out design with a glued pocket where we can put individual data sheets for each of our surfaces. This is shown in the concept design attached.

The concept designs are marked as outsidesheets and insidesheets in the uploads. We really like the timeline idea which shows we are involved at all stages of the project and not just at the analysis part.
Updates

Hi, I have uploaded a pdf called Kestrel glued pocket folder. This is our mock up layout to follow to give an idea of what we are after. Thanks, Alan

Hi, I have added some more stock images to the picture library which can be used in the designs. Thanks, Alan

Target Market(s)

Engineers, project managers

Industry/Entity Type

Oil And Gas

Colors
ec2027

Requirements
Must have
• Overall:
3 pages
Triangle glued pocket, business card holder
Quality policy on the pocket
Attached are selected images which the designer can use and edit at their own discretion.

Outer sheets :
Keep current front page with Kestrel banner and energy engineering
Map on rear page and contact email address
Feature sheet with big picture and energy engineering tag line

Inner sheet
Timeline feature on the top showing our involvement from site survey and scan to installation and commissioning, with pictures on each stage.

A first inner page with our what we do text and services

A USPs page with all our key facts and figures.

Nice to have
• Map on the rear cover showing offices in Aberdeen, Houston, Dubai and Kuala Lumpur

```html
<!DOCTYPE html>
<html lang="en">
<head>
<meta charset="utf-8">
<title>Kestrel Ridge Systems – Inside Spread</title>
<link href="https://fonts.googleapis.com/css2?family=Open+Sans:wght@400;600;700&display=swap" rel="stylesheet">
<style>
  :root{
    --red:#ec2027;
    --grey:#9a9a9a;
    --ink:#555555;
    --white:#ffffff;
  }
  *{margin:0;padding:0;box-sizing:border-box}
  html,body{width:1200px;height:432px;overflow:hidden;background:var(--white)}
  body{font-family:"Open Sans",Arial,sans-serif;color:var(--grey)}
  .spread{position:relative;width:1200px;height:432px;overflow:hidden}

  /* timeline */
  .timeline{position:absolute;left:0;top:0;width:800px;height:60px;display:flex}
  .stage{position:relative;width:100px;height:58px;font-size:5px;line-height:1.3;color:var(--grey)}
  .stage::before{content:"";position:absolute;left:2px;top:8px;width:10px;height:44px;
    background:linear-gradient(90deg,#e0e0e0,#f4f4f4);clip-path:polygon(0 0,40% 0,100% 50%,40% 100%,0 100%,60% 50%)}
  .stage-label{position:absolute;left:16px;top:20px;width:36px}
  .stage-pic{position:absolute;left:56px;top:14px;width:40px;height:40px;border-radius:3px}
  .rule{position:absolute;left:0;top:59px;width:830px;height:2px;background:var(--red)}

  /* intro column */
  .intro{position:absolute;left:60px;top:120px;width:260px;font-size:5.4px;line-height:1.45}
  .intro h2{color:var(--red);font-size:6.6px;font-weight:600;margin-bottom:2px}
  .intro p{width:240px;margin-bottom:10px}
  .lists{display:flex;gap:14px}
  .lists .col{width:90px}
  .lists .col.wide{width:115px}
  .lists ul{list-style:none;margin-bottom:9px}
  .lists li{padding-left:6px;position:relative}
  .lists li::before{content:"•";position:absolute;left:0}

  /* brand */
  .brand{position:absolute;left:34px;top:324px;display:flex;flex-direction:column;align-items:flex-start}
  .brand .mark{width:22px;height:22px;background:var(--red);margin-left:14px;margin-bottom:4px}
  .brand .name{font-size:9px;font-weight:600;letter-spacing:2px;color:var(--ink)}
  .brand .tag{font-size:3.6px;color:var(--ink);letter-spacing:.3px;margin-top:1px}

  /* figures */
  .fig{position:absolute;font-size:5.2px;line-height:1.3;color:var(--grey)}
  .fig strong{display:block;color:var(--red);font-size:8.4px;font-weight:700}
  .segment{position:absolute;left:324px;top:300px;width:110px;font-size:5.6px;line-height:1.3}

  .scene{position:absolute;left:318px;top:96px}

  .band{position:absolute;left:0;top:390px;width:640px;height:20px;background:var(--red)}
  .pocket{position:absolute;left:0;top:0}
</style>
</head>
<body>
<div class="spread">

  <nav class="timeline">
    <div class="stage"><span class="stage-label">Site survey &amp; laser scan</span><div class="stage-pic" role="img" aria-label="Laser scanner on tripod" style="background:linear-gradient(#b8b8b8,#6e6e6e)"></div></div>
    <div class="stage"><span class="stage-label">Model build</span><div class="stage-pic" role="img" aria-label="Green 3D pipework model" style="background:linear-gradient(#7fc36a,#2f7d2b)"></div></div>
    <div class="stage"><span class="stage-label">Analysis</span><div class="stage-pic" role="img" aria-label="Colour contour analysis plot" style="background:linear-gradient(90deg,#2f6cd0,#3fd07a,#f0d03a,#e0402a)"></div></div>
    <div class="stage"><span class="stage-label">Concept design</span><div class="stage-pic" role="img" aria-label="Blue wireframe concept sketch" style="background:linear-gradient(#e8eef8,#b6c6e4)"></div></div>
    <div class="stage"><span class="stage-label">Standards verification</span><div class="stage-pic" role="img" aria-label="Vernier caliper" style="background:linear-gradient(#d8dbe6,#8088a8)"></div></div>
    <div class="stage"><span class="stage-label">Detailed design</span><div class="stage-pic" role="img" aria-label="Red skid detailed design" style="background:linear-gradient(#d04040,#8a1a1a)"></div></div>
    <div class="stage"><span class="stage-label">Fabrication Management</span><div class="stage-pic" role="img" aria-label="Fabrication equipment" style="background:linear-gradient(#c6cfe8,#4a5ea8)"></div></div>
    <div class="stage"><span class="stage-label">Installation &amp; commissioning support</span><div class="stage-pic" role="img" aria-label="Spanner and screwdriver icon" style="background:linear-gradient(#c8c8c8,#8a8a8a)"></div></div>
  </nav>
  <div class="rule"></div>

  <section class="intro">
    <h2>What We Do</h2>
    <p>Kestrel provides integrated, multi-disciplinary engineering design and analysis services to clients worldwide. It is a global division of Harlow Meridian Group and Northgate Energy Group Inc, operating within the international energy industries.</p>
    <div class="lists">
      <div class="col">
        <h2>Our Core Activities include:</h2>
        <ul>
          <li>Fire &amp; blast simulation</li>
          <li>Plume dispersion</li>
          <li>Offshore engineering</li>
          <li>Subsea engineering</li>
          <li>Pipeline engineering</li>
          <li>Emergency response engineering</li>
          <li>Process &amp; separation simulation</li>
          <li>Renewables engineering</li>
          <li>Product design &amp; development</li>
        </ul>
      </div>
      <div class="col wide">
        <h2>Our Core Services include:</h2>
        <ul>
          <li>Flow assurance and thermal engineering</li>
          <li>Multiphase flow and computational fluid dynamics (CFD)</li>
          <li>Multi-physics simulations</li>
          <li>Structural &amp; mechanical design engineering</li>
          <li>Advanced structural finite element analysis (FEA)</li>
          <li>Marine dynamics and installation engineering</li>
        </ul>
        <h2>Our technologies include</h2>
        <ul>
          <li>Computational Fluid Dynamics (CFD)</li>
          <li>Finite Element Analysis (FEA)</li>
          <li>Computer Aided Engineering (CAE)</li>
        </ul>
      </div>
    </div>
  </section>

  <div class="brand">
    <div class="mark"></div>
    <div class="name">KESTREL</div>
    <div class="tag">A NORTHGATE ENERGY GROUP COMPANY</div>
  </div>

  <div class="fig" style="left:324px;top:82px"><strong>72,000</strong>Devices fitted and installed in 2013</div>
  <div class="fig" style="left:486px;top:82px"><strong>5,000+</strong>Successfully completed projects</div>
  <div class="fig" style="left:654px;top:82px;width:90px"><strong>350,000+</strong>Total hours work as engineering consultants</div>

  <svg class="scene" width="420" height="250" viewBox="0 0 420 250" role="img" aria-label="Cutaway illustration of offshore platforms, seabed and subsea pipelines">
    <defs>
      <linearGradient id="sea" x1="0" y1="0" x2="0" y2="1">
        <stop offset="0" stop-color="#8fc8d0"/><stop offset=".55" stop-color="#3f8e9c"/><stop offset="1" stop-color="#8a7c66"/>
      </linearGradient>
    </defs>
    <polygon points="4,38 210,18 412,42 412,156 336,240 4,138" fill="url(#sea)"/>
  </svg>

  <div class="segment">A business segment of Northgate Energy Group, a group with:</div>
  <div class="fig" style="left:324px;top:322px"><strong>14,000</strong>Employees</div>
  <div class="fig" style="left:324px;top:342px"><strong>$4 billion</strong>In revenues</div>
  <div class="fig" style="left:402px;top:342px;width:110px"><strong>40%</strong>Re-investment of business into research and development</div>
  <div class="fig" style="left:516px;top:342px;width:100px"><strong>No.1</strong>Preferred design and analysis consultants</div>

  <div class="band"></div>

  <svg class="pocket" width="1200" height="432" viewBox="0 0 1200 432" aria-hidden="true">
    <polygon points="846,0 912,0 912,406 902,432 646,432 626,406" fill="var(--red)"/>
    <polygon points="914,0 960,0 1200,406 1200,432 926,432 914,406" fill="var(--red)"/>
  </svg>
</div>
</body>
</html>
```